Business Card Design Project

We need a business card design for a company based in San Francisco called PlanGlide. PlanGlide makes customized academic planners for high schools and middle schools. Currently we sell directly to the schools who either re-sell or give the planners to their students. The planners are designed to help students stay organized and manage their time. The books are unique in that they are made individually for each school and include the school's events, student artwork and most importantly the daily class schedule in each week. This helps the student to understand what classes they have each day and what homework they need to do each night.

Currently the product is B:B; however, we are exploring ways in which to make this a B:C. Please review website at www.planglide.net

The final design should communicate time management and organization.

Card should be one-sided

Information for the business card should include

Dorothy Kellner Voss
Founder
dorothy@planglide.net
415-836-1752

Target Market(s)

High school and middle school administrators

Industry/Entity Type

School

Requirements
Must have
• One sided design
Nice to have
• I'm open to new interpretations of the logo as well as color usage. I'm also open to changing the font of the logo type.
Should not have
• Please use a san serif font.

```html
<!DOCTYPE html>
<html lang="en">
<head>
<meta charset="utf-8">
<title>PlanGlide Business Card</title>
<link rel="stylesheet" href="https://fonts.googleapis.com/css2?family=Fira+Sans:wght@400;500;600&display=swap">
<style>
  :root {
    --backdrop: #e9e9e9;
    --card: #ffffff;
    --ink: #1f1f1f;
    --accent: #d71f3a;
    --rule: #bdbdbd;
    --stripe: #111111;
  }
  * { margin: 0; padding: 0; box-sizing: border-box; }
  html, body {
    width: 1200px; height: 799px; overflow: hidden;
    background: var(--backdrop);
    font-family: "Fira Sans", sans-serif;
    color: var(--ink);
  }
  .business-card {
    position: absolute; left: 150px; top: 150px;
    width: 900px; height: 500px;
    background: var(--card);
    box-shadow: 0 6px 24px rgba(0,0,0,0.12);
    overflow: hidden;
  }
  .brand { position: absolute; left: 52px; top: 196px; }
  .brand-name {
    font-size: 44px; font-weight: 400; letter-spacing: -0.5px; line-height: 1;
    color: var(--ink);
  }
  .brand-tagline {
    margin-top: 10px; padding-left: 4px;
    font-size: 20px; color: var(--accent); letter-spacing: 0.2px;
  }
  .divider {
    position: absolute; left: 422px; top: 105px;
    width: 2px; height: 320px; background: var(--rule);
  }
  .contact { position: absolute; left: 452px; top: 106px; }
  .person-name { font-size: 26px; font-weight: 600; color: var(--accent); line-height: 1.1; }
  .person-title { font-size: 21px; margin-top: 4px; }
  .address { margin-top: 40px; font-size: 24px; line-height: 36px; }
  .details { list-style: none; margin-top: 30px; font-size: 24px; }
  .details li { display: flex; align-items: center; gap: 8px; height: 36px; }
  .details svg { width: 20px; height: 20px; flex: none; }
  .band { position: absolute; left: 0; bottom: 0; width: 900px; height: 57px; }
</style>
</head>
<body>
  <div class="business-card">
    <div class="brand">
      <div class="brand-name">PlanGlide</div>
      <div class="brand-tagline">Customized Academic Planners</div>
    </div>

    <div class="divider"></div>

    <div class="contact">
      <div class="person-name">Dorothy Kellner Voss</div>
      <div class="person-title">Founder</div>
      <div class="address">2817 Dunmore St, Hillcrest<br>San Francisco</div>
      <ul class="details">
        <li>
          <svg viewBox="0 0 20 20" aria-hidden="true"><circle cx="10" cy="10" r="8.5" fill="none" stroke="var(--accent)" stroke-width="1.6"/><path d="M7 5.5c-1 1.5 0 5 2.5 7.5s5 3 6 2l-1.8-2-1.6 1c-1.5-.8-3-2.5-3.6-4l1-1.5z" fill="var(--accent)"/></svg>
          415-836-1752
        </li>
        <li>
          <svg viewBox="0 0 20 20" aria-hidden="true"><rect x="1" y="4" width="18" height="12" fill="var(--accent)"/><path d="M1 4l9 7 9-7" fill="none" stroke="#fff" stroke-width="1.5"/></svg>
          dorothy@planglide.net
        </li>
        <li>
          <svg viewBox="0 0 20 20" aria-hidden="true" fill="none" stroke="var(--accent)" stroke-width="1.4"><circle cx="10" cy="10" r="8.5"/><ellipse cx="10" cy="10" rx="3.8" ry="8.5"/><path d="M1.5 10h17M3 5.5h14M3 14.5h14"/></svg>
          www.planglide.net
        </li>
      </ul>
    </div>

    <svg class="band" viewBox="0 0 900 57" aria-hidden="true">
      <polygon points="0,12 512,12 506,25 0,25" fill="var(--stripe)"/>
      <polygon points="530,0 900,0 900,57 0,57 0,30 518,30" fill="var(--accent)"/>
    </svg>
  </div>
</body>
</html>
```